Book cover design for modern bagpipe music book

This music book will be A4 in size and requires a design for the front and back cover. The focus is on creating a modern and eye catching design, breaking away from the stereotypes of what people think of when they think of bagpipes. Think the OPPOSITE of a bagpiper in a full kilt standing on top of a mountain playing Copper Lanterns Rising!

Book title: Rise Hum March Rest

Other front cover text : Music for the bagpipes by Dermot Fairley

Front cover file ideas uploaded

2 pictures of bagpipes attached.

- The real set of bagpipes give an idea of the correct finer details

- The toy bagpipes perhaps have a better shape with the left 'stick' down

Back cover - No real brief. Keen for it not to be a full block single colour though.

Design requires 3mm bleed for print

Open to ideas and suggestions! Thank you!

```html
<!DOCTYPE html>
<html lang="en">
<head>
<meta charset="utf-8">
<title>Rise Hum March Rest — Music for the Bagpipes</title>
<link rel="stylesheet" href="https://fonts.googleapis.com/css2?family=Bebas+Neue&family=Montserrat:wght@300;800&display=swap">
<style>
  :root {
    --navy: #243447;
    --teal: #3dbfbc;
    --green: #a0cb3a;
    --red: #ee3a24;
    --navy-soft: #dfe3e8;
    --teal-soft: #e0f4f3;
    --green-soft: #eef6dc;
    --red-soft: #fde3df;
    --ink: #111111;
    --paper: #ffffff;
  }
  html, body {
    margin: 0;
    padding: 0;
    width: 886px;
    height: 1200px;
    overflow: hidden;
    background: var(--paper);
  }
  .cover {
    position: relative;
    width: 886px;
    height: 1200px;
    overflow: hidden;
    background: var(--paper);
  }
  .emblems {
    position: absolute;
    left: 0;
    top: 0;
    width: 886px;
    height: 1200px;
  }
  .title {
    margin: 0;
    font-weight: 400;
  }
  .title-word {
    position: absolute;
    left: 345px;
    font-family: "Bebas Neue", "Oswald", sans-serif;
    font-size: 197px;
    line-height: 1;
    letter-spacing: 1px;
    white-space: nowrap;
  }
  .title-word--rise  { top: 89px;  color: var(--navy); }
  .title-word--hum   { top: 320px; color: var(--teal); }
  .title-word--march { top: 549px; color: var(--green); }
  .title-word--rest  { top: 789px; color: var(--red); }
  .subtitle, .byline {
    position: absolute;
    left: 0;
    width: 940px;
    margin: 0;
    text-align: center;
    font-family: "Montserrat", "Helvetica Neue", sans-serif;
    color: var(--ink);
    line-height: 1;
    white-space: nowrap;
  }
  .subtitle {
    top: 1044px;
    font-weight: 300;
    font-size: 46px;
    letter-spacing: -1px;
  }
  .byline {
    top: 1106px;
    font-weight: 800;
    font-size: 43px;
    letter-spacing: -1px;
  }
</style>
</head>
<body>
<main class="cover">
  <svg class="emblems" viewBox="0 0 886 1200">
    <g class="emblem emblem--rise">
      <circle cx="193" cy="175" r="97" fill="none" stroke="var(--navy)" stroke-width="11"/>
      <circle cx="193" cy="175" r="70" fill="var(--navy-soft)" role="img" aria-label="Morning icon"/>
    </g>
    <g class="emblem emblem--hum">
      <circle cx="193" cy="404" r="97" fill="none" stroke="var(--teal)" stroke-width="11"/>
      <circle cx="193" cy="404" r="70" fill="var(--teal-soft)" role="img" aria-label="Humming icon"/>
    </g>
    <g class="emblem emblem--march">
      <circle cx="193" cy="633" r="97" fill="none" stroke="var(--green)" stroke-width="11"/>
      <circle cx="193" cy="633" r="70" fill="var(--green-soft)" role="img" aria-label="Bagpipes icon"/>
    </g>
    <g class="emblem emblem--rest">
      <circle cx="193" cy="862" r="97" fill="none" stroke="var(--red)" stroke-width="11"/>
      <circle cx="193" cy="862" r="70" fill="var(--red-soft)" role="img" aria-label="Resting icon"/>
    </g>
  </svg>

  <h1 class="title">
    <span class="title-word title-word--rise">RISE</span>
    <span class="title-word title-word--hum">HUM</span>
    <span class="title-word title-word--march">MARCH</span>
    <span class="title-word title-word--rest">REST</span>
  </h1>
  <p class="subtitle">MUSIC FOR THE BAGPIPES</p>
  <p class="byline">BY DERMOT FAIRLEY</p>
</main>
</body>
</html>
```